Bright Pathway! A website showcasing who I am as a person

Bright Pathway started out as idea for me to better myself as a person and work on small projects that would help me grow as a person. Now I want to build a website showcasing "Bright Pathway." I want the website to showcase who I am and how I have grown both professionally and personally. I can build the raw code of the website on my own but I am not really much of a designer. I am looking for a design where I can write and post blogs, articles and share my thoughts. A little about myself and the ideas and interests that I want to share
What is Bright Pathway
Who I am
Background - Professional
Brand Marketing
Email Automation
Hiking
Rock Climbing
Traveling
Exercising and Transformation
"Personal Thoughts"
Hopefully this is enough information to get people started on some designs.
Work
3 page

```html
<!DOCTYPE html>
<html lang="en">
<head>
<meta charset="utf-8">
<title>Rohan Mehra — Bright Pathway</title>
<link href="https://fonts.googleapis.com/css2?family=Montserrat:wght@400;500;600;700&display=swap" rel="stylesheet">
<style>
:root{
  --blue:#2f73b8;
  --blue-dark:#245f9c;
  --ink:#222;
  --muted:#666;
  --white:#fff;
  --footer-bg:#f0f0f0;
  --line:#dcdcdc;
}
*{box-sizing:border-box;margin:0;padding:0}
html,body{width:1200px;height:4000px;overflow:hidden;background:var(--white)}
body{font-family:'Montserrat',Arial,sans-serif;color:var(--ink);position:relative}

.site-header{position:absolute;top:0;left:0;width:1200px;height:88px}
.brand{position:absolute;left:128px;top:28px;font-size:30px;font-weight:600;letter-spacing:2px;color:var(--blue);text-transform:uppercase}
.header-cta{position:absolute;left:869px;top:24px;width:208px;height:40px;border:2px solid var(--blue);color:var(--blue);font-size:14px;font-weight:500;display:flex;align-items:center;justify-content:center;letter-spacing:.5px;text-transform:uppercase}

.main-nav{position:absolute;top:88px;left:0;width:1200px;height:35px;background:var(--blue);display:flex;align-items:center;justify-content:space-between;padding:0 14px}
.main-nav span{color:var(--white);font-size:11px;font-weight:600;text-transform:uppercase;letter-spacing:.2px}

.hero{position:absolute;top:123px;left:0;width:1200px;height:544px;background:linear-gradient(100deg,#3f6a74 0%,#5e8a92 35%,#8aa5ab 60%,#c9d2d3 100%)}
.hero-title{position:absolute;left:128px;top:120px;color:var(--white);font-size:50px;font-weight:600;text-transform:uppercase;letter-spacing:1px}
.hero-quote{position:absolute;color:var(--white);font-size:90px;font-weight:700;line-height:1}
.hero-quote.open{left:128px;top:72px}
.hero-quote.close{left:420px;top:185px}
.hero-dots{position:absolute;left:0;right:0;top:516px;display:flex;justify-content:center;gap:14px}
.hero-dots i{width:9px;height:9px;border-radius:50%;background:var(--white);display:block}
.hero-dots i.active{background:transparent;border:2px solid var(--white);width:13px;height:13px;margin-top:-2px}

.section-title{position:absolute;left:128px;font-size:32px;font-weight:600;color:var(--blue);text-transform:uppercase;letter-spacing:1px}

.blog-grid{position:absolute;left:133px;top:805px;width:934px;display:grid;grid-template-columns:307px 307px 288px;grid-template-rows:repeat(6,219px);gap:16px}
.post{position:relative;overflow:hidden}
.post .photo{position:absolute;inset:0}
.post .shade{position:absolute;inset:0;background:linear-gradient(to bottom,rgba(0,0,0,0) 45%,rgba(0,0,0,.7) 100%)}
.post .meta{position:absolute;left:22px;right:16px;bottom:14px;color:var(--white)}
.date{display:inline-block;background:var(--blue);color:var(--white);font-size:10px;padding:4px 8px;margin-bottom:8px}
.post h3{font-size:20px;font-weight:700;text-transform:uppercase;letter-spacing:.5px;line-height:1.1}
.post.feature h3{font-size:21px}
.post p{font-size:12px;margin-top:5px;white-space:nowrap;overflow:hidden}
.span-big-1{grid-column:1/3;grid-row:1/3}
.span-big-2{grid-column:2/4;grid-row:4/6}

.article-grid{position:absolute;left:133px;top:2352px;width:934px;display:grid;grid-template-columns:repeat(3,293px);column-gap:27px;row-gap:31px}
.article{height:340px}
.article .photo{height:213px}
.article h4{font-size:13px;font-weight:700;text-transform:uppercase;line-height:1.35;margin-top:-6px;background:var(--white);width:265px;padding:8px 0 0 0;position:relative}
.article p{font-size:11px;color:var(--muted);line-height:1.6;margin-top:12px;width:270px}
.btn-small{display:inline-block;background:var(--blue);color:var(--white);font-size:10px;font-weight:600;text-transform:uppercase;padding:7px 12px;margin-top:12px}

.load-more{position:absolute;left:536px;top:3491px;width:125px;height:38px;border:1px solid var(--line);color:var(--blue);font-size:12px;font-weight:600;text-transform:uppercase;display:flex;align-items:center;justify-content:center;letter-spacing:.5px}

.site-footer{position:absolute;left:0;top:3597px;width:1200px;height:403px;background:var(--footer-bg)}
.footer-brand{position:absolute;left:131px;top:72px;font-size:28px;font-weight:600;color:var(--blue);letter-spacing:2px;text-transform:uppercase}
.follow{position:absolute;left:131px;top:144px;width:260px;text-align:center;font-size:11px;font-weight:600;text-transform:uppercase}
.social{position:absolute;left:186px;top:178px;display:flex;gap:9px}
.social i{display:block;width:32px;height:32px;border-radius:50%;background:var(--blue)}
.footer-heading{position:absolute;top:66px;font-size:12px;font-weight:700;text-transform:uppercase}
.menu-col{position:absolute;top:106px;list-style:none;font-size:12px;color:#444;line-height:23px}
.newsletter-input{position:absolute;left:813px;top:102px;width:256px;height:52px;border:2px solid #333;background:var(--white);display:flex;align-items:center;padding-left:22px;gap:18px;font-size:12px;color:#555}
.newsletter-submit{position:absolute;left:963px;top:174px;width:106px;height:40px;background:var(--blue);color:var(--white);font-size:13px;font-weight:600;text-transform:uppercase;display:flex;align-items:center;justify-content:center}
.footer-rule{position:absolute;left:131px;top:296px;width:938px;height:1px;background:var(--line)}
.copyright{position:absolute;left:0;width:1200px;top:338px;text-align:center;font-size:11px;color:#444}
</style>
</head>
<body>

<header class="site-header">
  <div class="brand">Rohan Mehra</div>
  <div class="header-cta">Personal Thoughts</div>
</header>

<nav class="main-nav">
  <span>What is Bright Pathway</span>
  <span>Who I am</span>
  <span>Background - Professional</span>
  <span>Brand Marketing</span>
  <span>Email Automation</span>
  <span>Hiking</span>
  <span>Rock Climbing</span>
  <span>Traveling</span>
  <span>Exercising and Transformation</span>
</nav>

<section class="hero" role="img" aria-label="Photo of a man in a suit driving a car">
  <div class="hero-quote open">“</div>
  <h1 class="hero-title">Bright Pathway</h1>
  <div class="hero-quote close">”</div>
  <div class="hero-dots"><i></i><i class="active"></i><i></i><i></i><i></i></div>
</section>

<h2 class="section-title" style="top:727px">Latest Blog</h2>

<section class="blog-grid">
  <article class="post feature span-big-1">
    <div class="photo" role="img" aria-label="Photo of a businessman in glasses at a laptop" style="background:linear-gradient(135deg,#e4e8ec,#b9c2cc 55%,#3d4d66)"></div>
    <div class="shade"></div>
    <div class="meta"><span class="date">02 May, 2017</span><h3>There are many variations of passages</h3><p>It is a long established fact that a reader will be distracted</p></div>
  </article>
  <article class="post">
    <div class="photo" role="img" aria-label="Photo of a woman in glasses" style="background:linear-gradient(135deg,#d6dbe0,#7d8a9a 60%,#3e3b45)"></div>
    <div class="shade"></div>
    <div class="meta"><span class="date">02 May, 2017</span><h3>Heading 1</h3><p>It is a long established reader will be</p></div>
  </article>
  <article class="post">
    <div class="photo" role="img" aria-label="Photo of a man working at an office desk" style="background:linear-gradient(135deg,#f1f1f1,#b7bcc4 55%,#4a5566)"></div>
    <div class="shade"></div>
    <div class="meta"><span class="date">02 May, 2017</span><h3>Heading 2</h3><p>It is a long established reader will be</p></div>
  </article>
  <article class="post">
    <div class="photo" role="img" aria-label="Photo of a city skyline at sunset" style="background:linear-gradient(180deg,#6a5a8a,#d97a4c 55%,#2b2b3a)"></div>
    <div class="shade"></div>
    <div class="meta"><span class="date">02 May, 2017</span><h3>Heading 5</h3><p>It is a long established reader will be</p></div>
  </article>
  <article class="post">
    <div class="photo" role="img" aria-label="Photo of hands joined together in a circle" style="background:linear-gradient(135deg,#8a6a4c,#c5a27c 50%,#4a3a30)"></div>
    <div class="shade"></div>
    <div class="meta"><span class="date">02 May, 2017</span><h3>Heading 4</h3><p>It is a long established reader will be</p></div>
  </article>
  <article class="post">
    <div class="photo" role="img" aria-label="Photo of hands holding a smartphone" style="background:linear-gradient(135deg,#e3a862,#c8714a 55%,#5a3a2e)"></div>
    <div class="shade"></div>
    <div class="meta"><span class="date">02 May, 2017</span><h3>Heading 3</h3><p>It is a long established reader will be</p></div>
  </article>
  <article class="post">
    <div class="photo" role="img" aria-label="Photo of a smiling businesswoman in an office" style="background:linear-gradient(135deg,#cfc8bf,#8c8680 55%,#3c3a3a)"></div>
    <div class="shade"></div>
    <div class="meta"><span class="date">02 May, 2017</span><h3>Heading 6</h3><p>It is a long established reader will be</p></div>
  </article>
  <article class="post feature span-big-2">
    <div class="photo" role="img" aria-label="Photo of a man with a laptop and suitcase giving thumbs up" style="background:linear-gradient(135deg,#f0ece6,#c9c1b4 50%,#5a5550)"></div>
    <div class="shade"></div>
    <div class="meta"><span class="date">02 May, 2017</span><h3>There are many variations of passages</h3><p>It is a long established fact that a reader will be distracted</p></div>
  </article>
  <article class="post">
    <div class="photo" role="img" aria-label="Photo of a group of colleagues" style="background:linear-gradient(135deg,#d9d6d2,#8f8880 55%,#2f2f35)"></div>
    <div class="shade"></div>
    <div class="meta"><span class="date">02 May, 2017</span><h3>Heading 7</h3><p>It is a long established reader will be</p></div>
  </article>
  <article class="post">
    <div class="photo" role="img" aria-label="Photo of a man relaxing at his desk" style="background:linear-gradient(135deg,#b9a48c,#8a7662 55%,#3a3230)"></div>
    <div class="shade"></div>
    <div class="meta"><span class="date">02 May, 2017</span><h3>Heading 8</h3><p>It is a long established reader will be</p></div>
  </article>
  <article class="post">
    <div class="photo" role="img" aria-label="Photo of hands holding a phone in warm light" style="background:linear-gradient(135deg,#f1c27a,#d98b52 55%,#5a3a2e)"></div>
    <div class="shade"></div>
    <div class="meta"><span class="date">02 May, 2017</span><h3>Heading 9</h3><p>It is a long established reader will be</p></div>
  </article>
  <article class="post">
    <div class="photo" role="img" aria-label="Photo of a smiling man at a desk" style="background:linear-gradient(135deg,#e6e2dc,#a8a39c 55%,#4a4644)"></div>
    <div class="shade"></div>
    <div class="meta"><span class="date">02 May, 2017</span><h3>Heading 10</h3><p>It is a long established reader will be</p></div>
  </article>
</section>

<h2 class="section-title" style="top:2262px">Latest Articles</h2>

<section class="article-grid">
  <article class="article">
    <div class="photo" role="img" aria-label="Photo of friends celebrating outdoors" style="background:linear-gradient(135deg,#9cc6e8,#d9b48a 55%,#6a4a3a)"></div>
    <h4>There are many variations<br>of passages</h4>
    <p>It is a long established fact that a reader will be distracted by the readable</p>
    <span class="btn-small">Read more</span>
  </article>
  <article class="article">
    <div class="photo" role="img" aria-label="Photo of a smiling senior businessman" style="background:linear-gradient(135deg,#eef2f5,#b8c4cf 55%,#4c5a6c)"></div>
    <h4>Contrary to popular belief,<br>orem ipsum is not simply</h4>
    <p>It is a long established fact that a reader will be distracted by the readable</p>
    <span class="btn-small">Read more</span>
  </article>
  <article class="article">
    <div class="photo" role="img" aria-label="Photo of a business meeting in a bright office" style="background:linear-gradient(135deg,#f4f6f7,#c4ccd2 55%,#5a6470)"></div>
    <h4>But I must explain to you how<br>all this mistaken idea</h4>
    <p>It is a long established fact that a reader will be distracted by the readable</p>
    <span class="btn-small">Read more</span>
  </article>
  <article class="article">
    <div class="photo" role="img" aria-label="Photo of a team stacking hands" style="background:linear-gradient(135deg,#a8b6c4,#7a8898 55%,#3a4452)"></div>
    <h4>There are many variations<br>of passages</h4>
    <p>It is a long established fact that a reader will be distracted by the readable</p>
    <span class="btn-small">Read more</span>
  </article>
  <article class="article">
    <div class="photo" role="img" aria-label="Photo of colleagues around a meeting table" style="background:linear-gradient(135deg,#6c8494,#a4b4be 55%,#3a4650)"></div>
    <h4>Contrary to popular belief,<br>orem ipsum is not simply</h4>
    <p>It is a long established fact that a reader will be distracted by the readable</p>
    <span class="btn-small">Read more</span>
  </article>
  <article class="article">
    <div class="photo" role="img" aria-label="Photo of a business team standing together" style="background:linear-gradient(135deg,#f2f2f2,#9aa0a8 55%,#2c3038)"></div>
    <h4>But I must explain to you how<br>all this mistaken idea</h4>
    <p>It is a long established fact that a reader will be distracted by the readable</p>
    <span class="btn-small">Read more</span>
  </article>
  <article class="article">
    <div class="photo" role="img" aria-label="Photo of a businessman in a suit" style="background:linear-gradient(135deg,#c8ccd0,#6a727c 55%,#262a32)"></div>
    <h4>There are many variations<br>of passages</h4>
    <p>It is a long established fact that a reader will be distracted by the readable</p>
    <span class="btn-small">Read more</span>
  </article>
  <article class="article">
    <div class="photo" role="img" aria-label="Photo of a woman using a tablet" style="background:linear-gradient(135deg,#ede6dc,#c6b49c 55%,#5a4a3c)"></div>
    <h4>Contrary to popular belief,<br>orem ipsum is not simply</h4>
    <p>It is a long established fact that a reader will be distracted by the readable</p>
    <span class="btn-small">Read more</span>
  </article>
  <article class="article">
    <div class="photo" role="img" aria-label="Photo of hands working on a laptop" style="background:linear-gradient(135deg,#dfe3e6,#8a96a2 55%,#2e3844)"></div>
    <h4>But I must explain to you how<br>all this mistaken idea</h4>
    <p>It is a long established fact that a reader will be distracted by the readable</p>
    <span class="btn-small">Read more</span>
  </article>
</section>

<div class="load-more">Load more</div>

<footer class="site-footer">
  <div class="footer-brand">Rohan Mehra</div>
  <div class="follow">Follow us</div>
  <div class="social"><i></i><i></i><i></i><i></i></div>

  <div class="footer-heading" style="left:445px">Menu</div>
  <ul class="menu-col" style="left:445px">
    <li>What is Bright Pathway</li>
    <li>Who I am</li>
    <li>Background - Professional</li>
    <li>Brand Marketing</li>
    <li>Email Automation</li>
    <li>Hiking</li>
  </ul>
  <ul class="menu-col" style="left:597px">
    <li>Rock Climbing</li>
    <li>Traveling</li>
    <li>Exercising and Transformation</li>
    <li>"Personal Thoughts"</li>
  </ul>

  <div class="footer-heading" style="left:813px">Newsletter Signup</div>
  <div class="newsletter-input">
    <svg width="16" height="12" viewBox="0 0 16 12" aria-hidden="true"><rect x="0.75" y="0.75" width="14.5" height="10.5" fill="none" stroke="#777" stroke-width="1.5"/><path d="M1 1l7 6 7-6" fill="none" stroke="#777" stroke-width="1.5"/></svg>
    <span>E-mail id</span>
  </div>
  <div class="newsletter-submit">Submit</div>

  <div class="footer-rule"></div>
  <div class="copyright">Copyrights @ 2017 All Rights Reserved</div>
</footer>

</body>
</html>
```